Healer at the Hearth needs business card

We need a business card that reflects the look and feel of the new website at www.healerathearth.ca

Target Market(s)

Our patient navigation and advocacy services are most commonly used by seniors who feel overwhelmed by the health care system and want someone on their side to advocate for their care. Individuals with ill parents or other family members may also come to rely on Healer at the Hearth to help them support their loved one through their health care journey. Ultimately, anyone who finds their health care experience challenging and wants someone completely focused on their needs can benefit from the services of our doctor / nurse team.

Industry/Entity Type

Business

Requirements
Must have
• One design tailored for two clinician which should include: logo, name, title, tel, email, web address and tagline
Nice to have
• A banner image to create a similar look to the website at www.healerathearth.ca
Should not have
• Too cluttered or busy - must be clean and professional

```html
<!DOCTYPE html>
<html lang="en">
<head>
<meta charset="utf-8">
<title>Healer at the Hearth — Business Card</title>
<link href="https://fonts.googleapis.com/css2?family=PT+Sans:wght@400;700&family=Arimo:wght@400&display=swap" rel="stylesheet">
<style>
  :root {
    --stage: #e9e7e3;
    --paper: #fbfbfa;
    --brand-red: #a3192a;
    --brand-blue: #2b5e8e;
    --ink: #1d1d1d;
    --muted: #4a4a4a;
    --faint-red: #efdcd6;
    --banner-light: #eeeeec;
    --banner-mid: #d9d8d4;
    --banner-red: #c8232c;
  }
  * { box-sizing: border-box; margin: 0; padding: 0; }
  html, body { width: 1200px; height: 1000px; overflow: hidden; }
  body {
    background: var(--stage);
    display: flex; flex-direction: column; align-items: center; justify-content: center;
    gap: 40px;
    font-family: "Arimo", Arial, sans-serif;
  }
  .card {
    position: relative;
    width: 800px; height: 457px;
    background: var(--paper);
    box-shadow: 0 4px 14px rgba(0,0,0,.12);
    overflow: hidden;
  }
  .brand {
    display: flex; align-items: center; gap: 12px;
    font-family: "PT Sans", sans-serif;
    color: var(--brand-blue);
    font-size: 34px; line-height: 1.0;
  }
  .brand-dot {
    width: 44px; height: 44px; border-radius: 50%;
    background: var(--brand-red); flex: none;
  }
  /* front */
  .card-front .brand { position: absolute; left: 250px; top: 70px; }
  .tagline {
    position: absolute; left: 0; right: 0; top: 168px;
    text-align: center;
    font-family: "PT Sans", sans-serif; font-size: 19px; color: var(--ink);
  }
  .banner {
    position: absolute; left: 40px; right: 40px; top: 222px; height: 140px;
    background: linear-gradient(90deg, var(--banner-light) 0%, var(--banner-mid) 30%, var(--banner-light) 45%, var(--banner-red) 55%, var(--banner-light) 68%, var(--banner-mid) 85%, var(--banner-light) 100%);
  }
  /* back */
  .watermark {
    position: absolute; left: 250px; top: 40px;
    width: 400px; height: 400px; border-radius: 50%;
    background: var(--faint-red);
  }
  .card-back .brand { position: absolute; right: 56px; top: 56px; font-size: 30px; }
  .person { position: absolute; left: 56px; top: 62px; }
  .person-name { font-size: 34px; color: var(--ink); letter-spacing: .5px; }
  .person-name .surname { color: var(--brand-red); }
  .person-title { font-size: 13px; color: var(--muted); margin-top: 4px; }
  .contacts { position: absolute; left: 56px; top: 200px; list-style: none; }
  .contacts li {
    display: flex; align-items: center; gap: 14px;
    font-size: 17px; color: var(--ink); margin-bottom: 14px;
  }
  .contacts svg { width: 18px; height: 18px; fill: none; stroke: var(--muted); stroke-width: 1.6; flex: none; }
</style>
</head>
<body>
  <section class="card card-front">
    <div class="brand"><span class="brand-dot"></span><span>Healer at<br>the Hearth</span></div>
    <p class="tagline">Best Possible Health Care for You and Your Loved Ones</p>
    <div class="banner" role="img" aria-label="Banner photo of a doctor's white coat and stethoscope holding a red heart"></div>
  </section>

  <section class="card card-back">
    <div class="watermark"></div>
    <div class="person">
      <h1 class="person-name">Dr. Martin <span class="surname">Alvey</span></h1>
      <p class="person-title">MD, CO-FOUNDER</p>
    </div>
    <div class="brand"><span class="brand-dot"></span><span>Healer at<br>the Hearth</span></div>
    <ul class="contacts">
      <li><svg viewBox="0 0 18 18"><rect x="5" y="2" width="8" height="14" rx="1.5"/><line x1="8" y1="13.5" x2="10" y2="13.5"/></svg>+(1) 555-010-0000</li>
      <li><svg viewBox="0 0 18 18"><path d="M4 2.5l3 .5 1 3.5-2 1.5c1 2 2.5 3.5 4.5 4.5l1.5-2 3.5 1 .5 3c-6 1.5-13.5-6-12-12z"/></svg>+(1) 555-010-2498</li>
      <li><svg viewBox="0 0 18 18"><rect x="2" y="4" width="14" height="10"/><polyline points="2,4 9,10 16,4"/></svg>Martin_Alvey@healerathearth.ca</li>
      <li><svg viewBox="0 0 18 18"><circle cx="9" cy="9" r="7"/><ellipse cx="9" cy="9" rx="3" ry="7"/><line x1="2" y1="9" x2="16" y2="9"/></svg>http://www.healerathearth.ca</li>
    </ul>
  </section>
</body>
</html>
```